Building Company Business Card Design

Need a design for a business card:
It needs to have: Name, Phone, Facebook link, Website, email
i would also like a list of works we undertake:
-New Homes
-Extensions, Renovations & Bathrooms
-Decking, Carports, Sheds (Residential and Industrial)
-Carpentry
-Fences, Patios & Pergolas

Name, Phone, Facebook link, Website, email + details of services provided listed in description

```html
<!DOCTYPE html>
<html lang="en">
<head>
<meta charset="utf-8">
<title>Ridgeline Homes – Business Card</title>
<link href="https://fonts.googleapis.com/css2?family=Lato:wght@400;700;900&display=swap" rel="stylesheet">
<style>
  :root {
    --bg: #232323;
    --card: #1c1c1c;
    --green: #33b249;
    --grey: #8c8c8c;
    --light: #e9e9e9;
    --text: #cfcfcf;
  }
  * { box-sizing: border-box; margin: 0; padding: 0; }
  html, body { width: 1200px; height: 977px; overflow: hidden; }
  body {
    background: var(--bg);
    font-family: "Lato", sans-serif;
    position: relative;
  }
  .card {
    position: absolute;
    width: 560px;
    height: 320px;
    background: var(--card);
    border-radius: 18px;
    box-shadow: 0 4px 0 var(--green), 0 14px 30px rgba(0,0,0,.55);
    overflow: hidden;
  }
  .card-front { left: 60px; top: 110px; }
  .card-back { left: 580px; top: 530px; }

  .brand { display: flex; align-items: flex-start; gap: 10px; }
  .brand-square { width: 14px; height: 14px; background: var(--green); margin-top: 6px; flex: none; }
  .brand-name {
    font-weight: 700; color: var(--light); font-size: 26px; letter-spacing: 1px;
    text-transform: uppercase; line-height: 1.05; white-space: nowrap;
  }
  .brand-name small { display: block; font-size: 11.5px; letter-spacing: 1.2px; }

  .card-front .brand { position: absolute; left: 40px; top: 48px; }
  .services { position: absolute; left: 44px; top: 130px; list-style: none; }
  .services li {
    display: flex; gap: 10px; color: var(--text); font-size: 14px; letter-spacing: .5px;
    text-transform: uppercase; line-height: 1.2; margin-bottom: 9px;
  }
  .services svg { flex: none; margin-top: 1px; }

  .gloss-panel {
    position: absolute; right: 0; top: 0; width: 230px; height: 100%;
    background: linear-gradient(160deg, #6a6a6a 0%, #2c2c2c 35%, #0c0c0c 70%, #050505 100%);
  }

  .card-back .brand { position: absolute; left: 34px; top: 150px; }
  .card-back .brand-square { width: 12px; height: 12px; margin-top: 5px; }
  .card-back .brand-name { font-size: 22px; }
  .card-back .brand-name small { font-size: 9.8px; letter-spacing: 1px; }
  .divider { position: absolute; left: 300px; top: 36px; width: 1px; height: 240px; background: var(--green); }
  .contact { position: absolute; left: 322px; top: 44px; }
  .person-name { font-weight: 900; color: var(--grey); font-size: 24px; letter-spacing: .5px; text-transform: uppercase; white-space: nowrap; }
  .person-title { color: var(--green); font-size: 16px; margin-bottom: 16px; }
  .contact-row { display: flex; gap: 10px; color: var(--text); font-size: 13.5px; line-height: 1.35; margin-bottom: 8px; white-space: nowrap; }
  .contact-row svg { flex: none; margin-top: 2px; }
</style>
</head>
<body>

<section class="card card-front">
  <div class="brand">
    <span class="brand-square"></span>
    <div class="brand-name">Ridgeline Homes<small>and Developments Pty Ltd</small></div>
  </div>
  <ul class="services">
    <li><svg width="14" height="14" viewBox="0 0 14 14"><circle cx="7" cy="7" r="7" fill="var(--green)"/><path d="M3.8 7.2l2.1 2.1 4.3-4.4" stroke="#1c1c1c" stroke-width="1.8" fill="none"/></svg><span>New Homes</span></li>
    <li><svg width="14" height="14" viewBox="0 0 14 14"><circle cx="7" cy="7" r="7" fill="var(--green)"/><path d="M3.8 7.2l2.1 2.1 4.3-4.4" stroke="#1c1c1c" stroke-width="1.8" fill="none"/></svg><span>Extensions, Renovations<br>&amp; Bathrooms</span></li>
    <li><svg width="14" height="14" viewBox="0 0 14 14"><circle cx="7" cy="7" r="7" fill="var(--green)"/><path d="M3.8 7.2l2.1 2.1 4.3-4.4" stroke="#1c1c1c" stroke-width="1.8" fill="none"/></svg><span>Decking, Carports, Sheds<br>(Residential &amp; Industrial)</span></li>
    <li><svg width="14" height="14" viewBox="0 0 14 14"><circle cx="7" cy="7" r="7" fill="var(--green)"/><path d="M3.8 7.2l2.1 2.1 4.3-4.4" stroke="#1c1c1c" stroke-width="1.8" fill="none"/></svg><span>Carpentry</span></li>
    <li><svg width="14" height="14" viewBox="0 0 14 14"><circle cx="7" cy="7" r="7" fill="var(--green)"/><path d="M3.8 7.2l2.1 2.1 4.3-4.4" stroke="#1c1c1c" stroke-width="1.8" fill="none"/></svg><span>Fences, Patios<br>&amp; Pergolas</span></li>
  </ul>
  <div class="gloss-panel" role="img" aria-label="Glossy black decorative brand graphic"></div>
</section>

<section class="card card-back">
  <div class="brand">
    <span class="brand-square"></span>
    <div class="brand-name">Ridgeline Homes<small>and Developments Pty Ltd</small></div>
  </div>
  <div class="divider"></div>
  <div class="contact">
    <div class="person-name">Daniel Harper</div>
    <div class="person-title">Founder &amp; CEO</div>
    <div class="contact-row">
      <svg width="12" height="15" viewBox="0 0 12 15"><path d="M6 0a6 6 0 0 0-6 6c0 4.5 6 9 6 9s6-4.5 6-9a6 6 0 0 0-6-6z" fill="var(--green)"/><circle cx="6" cy="6" r="2.2" fill="#1c1c1c"/></svg>
      <span>Your Address, City<br>State, Zip 1235</span>
    </div>
    <div class="contact-row">
      <svg width="13" height="13" viewBox="0 0 24 24"><path d="M6.6 10.8a15.2 15.2 0 0 0 6.6 6.6l2.2-2.2a1 1 0 0 1 1-.25 11.4 11.4 0 0 0 3.6.57 1 1 0 0 1 1 1V20a1 1 0 0 1-1 1A17 17 0 0 1 3 4a1 1 0 0 1 1-1h3.5a1 1 0 0 1 1 1c0 1.250.2 2.450.57 3.6a1 1 0 0 1-.25 1z" fill="var(--green)"/></svg>
      <span>(123) 456-7890</span>
    </div>
    <div class="contact-row">
      <svg width="13" height="13" viewBox="0 0 14 14"><rect x="0" y="2.5" width="14" height="9.5" fill="var(--green)"/><path d="M0 2.5l7 5.2 7-5.2" stroke="#1c1c1c" stroke-width="1.3" fill="none"/></svg>
      <span>info@ridgelinehomes.com</span>
    </div>
    <div class="contact-row">
      <svg width="13" height="13" viewBox="0 0 14 14"><circle cx="7" cy="7" r="6" stroke="var(--green)" stroke-width="1.5" fill="none"/><ellipse cx="7" cy="7" rx="2.6" ry="6" stroke="var(--green)" stroke-width="1.2" fill="none"/><path d="M1 7h12" stroke="var(--green)" stroke-width="1.2"/></svg>
      <span>www.ridgelinehomes.com</span>
    </div>
    <div class="contact-row">
      <svg width="13" height="13" viewBox="0 0 14 14"><rect width="13" height="13" rx="2" fill="var(--green)"/></svg>
      <span>/ridgelinehomes</span>
    </div>
  </div>
</section>

</body>
</html>
```